Velm Biologics product brochure - credibility, sophistication, cutting-edge

Velm Biologics, Inc. is a company that provides the most cutting-edge regenerative medicine products in the US. This brochure will highlight our stem cell products VelmBase and VelmArc, educating the public/patients and physician alike on what stem cells are, comparison of various stem cell treatments available, and what makes Velm products different. This serves as a marketing tool to reach both patients and physicians.

I have included the current brochure, which I am not completely happy with. I want a brochure that portrays that we are a top-notch company, with credibility and sophistication. I will make slight content change, but most contents will stay.

Please refer to current website for further information: www.velmbiologics-example.com

Low design quality

Target Market(s)

doctors and patients.

Industry/Entity Type

Healthcare

Font styles to use
Serif
Other font styles liked:
• anything that looks best on brochures & easy to read

Colors

Designer to choose colors to be used in the design.

Requirements
Must have
• Clean & modern feel, eye-catching.
• Would prefer bi-fold rather than tri-fold, because I think it looks fresher.
• Easy to read, clear.
• beautiful, elegant, stunning
Should not have
• Please DO NOT recycle graphics or images from the old brochure. I would like this for sure to be brand new, fresh and original.

```html
<!DOCTYPE html>
<html lang="en">
<head>
<meta charset="utf-8">
<title>Velm Biologics – Stem Cells Brochure Page</title>
<link rel="stylesheet" href="https://fonts.googleapis.com/css2?family=Figtree:wght@400;500;600;700&family=Montserrat:wght@600;700&display=swap">
<style>
  :root{
    --gold:#f3c24e;
    --gold-deep:#ddaf5d;
    --gold-light:#f8cc52;
    --heading-bronze:#b57a37;
    --heading-gold:#d2982e;
    --accent:#d99a2a;
    --ink:#2d2d2d;
    --list-ink:#3a3224;
    --white:#ffffff;
    --page-bg:#ffffff;
  }
  *{margin:0;padding:0;box-sizing:border-box}
  html,body{width:1200px;height:1200px;overflow:hidden;background:var(--page-bg)}
  body{font-family:"Figtree",Arial,sans-serif;color:var(--ink);position:relative}
  .page{position:absolute;left:93px;top:80px;width:1019px;height:1034px;background:var(--white);
    box-shadow:4px 5px 6px rgba(0,0,0,.35)}

  .conditions-panel{position:absolute;left:107px;top:0;width:352px;height:742px;
    background:radial-gradient(ellipse 70% 60% at 55% 65%, var(--gold-light) 0%, var(--gold) 40%, var(--gold-deep) 100%);
    padding:105px 0 0 46px;color:var(--white)}
  .conditions-title{font-family:"Montserrat",Arial,sans-serif;font-weight:700;font-size:19px;line-height:25.6px;
    letter-spacing:-.2px;white-space:nowrap;margin-bottom:21px}
  .conditions-list{list-style:none;font-size:16px;line-height:19.6px;color:var(--list-ink);white-space:nowrap}
  .conditions-list li{position:relative;padding-left:9px}
  .conditions-list li::before{content:"";position:absolute;left:0;top:9px;width:3px;height:3px;border-radius:50%;background:var(--white)}

  .info-column{position:absolute;left:487px;top:106px;width:480px;font-size:14px;line-height:17.6px;white-space:nowrap}
  .info-column h2{font-family:"Montserrat",Arial,sans-serif;font-weight:700;font-size:19px;line-height:24px;letter-spacing:-.2px}
  .h-bronze{color:var(--heading-bronze)}
  .h-gold{color:var(--heading-gold);margin:10px 0 6px}
  .h-cord{margin-top:8px}
  .tagline{color:var(--accent);margin-bottom:5px}
  .info-column ul{list-style:none}
  .info-column li{position:relative;padding-left:9px}
  .info-column li::before{content:"";position:absolute;left:0;top:7.5px;width:3px;height:3px;border-radius:50%;background:var(--accent)}
  .plain-bullets li::before{background:var(--ink)}
  .note{color:var(--accent);line-height:19px}

  .photo{position:absolute;left:0;top:742px;width:459px;height:292px;
    background:linear-gradient(160deg,#d9d9d9 0%,#bdbdbd 45%,#6e6e6e 80%,#3d3d3d 100%)}
  .quality-box{position:absolute;left:459px;top:742px;width:560px;height:292px;
    background:linear-gradient(135deg,#f3c552,#f8ca52)}
  .diamond{position:absolute;left:0;top:742px;width:1019px;height:292px;overflow:visible}
  .quality-text{position:absolute;left:555px;top:801px;width:300px;text-align:center;color:var(--white);
    font-weight:500;font-size:16px;line-height:19.7px;white-space:nowrap}
</style>
</head>
<body>
<div class="page">
  <section class="conditions-panel">
    <h1 class="conditions-title">Currently stem cells have<br>been shown to have clinical<br>benefits in the following<br>conditions:</h1>
    <ul class="conditions-list">
      <li>Osteoarthritis</li>
      <li>Autoimmune Disorders (122<br>known, including Rheumatoid<br>Arthritis, Lupus, Crohn’s Disease,<br>Hashimoto’s Thyroiditis)</li>
      <li>Neurological Diseases<br>(Parkinson’s, Alzheimers, Multiple<br>Sclerosis, ALS, etc.)</li>
      <li>Type II Diabetes</li>
      <li>Heart Diseases</li>
      <li>Erectile Dysfunction</li>
      <li>Dermatological Disorders</li>
      <li>Lung Diseases (COPD, asthma, etc.)</li>
      <li>Athletic Injuries</li>
      <li>Autism</li>
      <li>Pain Management</li>
      <li>Spinal Cord Injuries</li>
      <li>Wound Care, Limb Salvage</li>
      <li>Anti-Aging (such as skin, hair,<br>energy improvement, etc.)</li>
    </ul>
  </section>

  <section class="info-column">
    <h2 class="h-bronze">Stem Cells</h2>
    <p class="tagline">self renewal, ability to differentiate, innate intelligence</p>
    <p>Every cell in our bodies can trace its origin to the ultimate stem cell<br>– a fertilized egg.</p>
    <ul class="plain-bullets">
      <li>Each cell division moves the cells down a path to their final cell type</li>
      <li>cells make commitments that are typically irreversible.</li>
      <li>our body requires stem cells for tissue regeneration</li>
    </ul>
    <h2 class="h-gold">Unique advantage of birth tissue stem cells:</h2>
    <ul>
      <li>Cells are young, more therapeutically active.</li>
      <li>Secret more growth factors, with higher speed of differentiation,<br>longer telomeres (more protected chromosomes), more future cell<br>generations, greater plasticity (i.e. able to differentiate into a more<br>diverse range of cell types).</li>
      <li>No matching necessary (these young cells have little surface<br>markers and are considered immune-privileged)</li>
      <li>convenient, consistent dosage, allows for higher and repeated<br>dosages</li>
      <li>excellent safety record</li>
      <li>robust angiogenic potential</li>
    </ul>
    <p class="note">These tissue transplant products are not classified as drugs by the<br>FDA as long as they are “minimally manipulated,” and must be used<br>for a homologous function.</p>
    <h2 class="h-bronze h-cord">Umbilical cord tissue</h2>
    <ul>
      <li>dense source of MSCs</li>
      <li>MSCs (mesenchymal stem cells) are regulatory cells, well<br>characterized clinically, with diverse differentiation potential, ideal<br>for inflammatory and degenerative diseases, and can activate local<br>stem cells.</li>
      <li>able to home in to areas of inflammation &amp; injury</li>
      <li>has anti-microbial &amp; anti-apoptotic (preventing programmed cell death)</li>
      <li>high anti-inflammatory &amp; immunomodulatory effect</li>
    </ul>
  </section>

  <div class="photo" role="img" aria-label="Black and white photo of a runner's legs on a road, with gold-tinted running shoes"></div>
  <div class="quality-box"></div>
  <svg class="diamond" viewBox="0 0 1019 292" aria-hidden="true">
    <polyline points="551,0 429,120 601,292" fill="none" stroke="#ffffff" stroke-width="1.6"/>
    <polyline points="861,0 983,120 811,292" fill="none" stroke="#ffffff" stroke-width="1.6"/>
  </svg>
  <p class="quality-text">Velm Biologics’ regenerative<br>medicine products are sourced<br>from an FDA registered &amp;<br>inspected, cGMP compliant<br>laboratory, which strictly follows<br>FDA &amp; AATB (American Association<br>of Tissue Banks) guideline, meeting<br>the highest of industry standard</p>
</div>
</body>
</html>
```